7Brink Plumbing flyer

I want to incorporate our logo design into a new flyer promoting the business and advertising products that we install.
We install hot water systems, Air-conditioning systems and central heating systems. Along with other aspects of plumbing such as gasfitting, roofing, sanitary and drainage
I would like the background to be the same as our business cards with the water effect and colours.

Requirements
Must have
• Logo
24/7 Emergency call out
Aspects of plumbing we do
- Hot water systems
- Central Heating
- Solar hot water systems/ heat pump systems
- Gasfitting
- Drainage
- Roofing
- Air-Conditioning
Nice to have
• Pictures of hot water systems and air-conditioning system
$30 off voucher when producing this flyer (limit 1 per house hold)

```html
<!DOCTYPE html>
<html lang="en">
<head>
<meta charset="utf-8">
<title>7Brink Plumbing Flyer</title>
<link rel="stylesheet" href="https://fonts.googleapis.com/css2?family=Roboto+Condensed:wght@400;700&display=swap">
<style>
  :root {
    --page: #e9e9e9;
    --dark: #2a2a2c;
    --dark-2: #343437;
    --blue: #1f86d6;
    --blue-deep: #1467b8;
    --blue-light: #41b0ec;
    --navy: #1c2a5e;
    --white: #ffffff;
  }
  * { box-sizing: border-box; margin: 0; padding: 0; }
  html, body { width: 1200px; height: 1200px; overflow: hidden; background: var(--page); }
  body { position: relative; font-family: "Roboto Condensed", sans-serif; color: var(--white); }

  .flyer {
    position: absolute; left: 197px; top: 30px;
    width: 925px; height: 1310px;
    transform: scale(0.8702); transform-origin: 0 0;
    background: radial-gradient(ellipse at 50% 30%, var(--dark-2), var(--dark) 70%);
    overflow: hidden;
  }
  .flyer-waves { position: absolute; inset: 0; }

  .brand { position: absolute; left: 160px; top: 100px; display: flex; align-items: center; gap: 26px; }
  .brand-dot { width: 120px; height: 120px; border-radius: 50%; background: var(--blue); flex: none; }
  .brand-name { color: var(--blue-light); font-weight: 700; line-height: 0.95; text-transform: uppercase; }
  .brand-name .l1 { display: block; font-size: 78px; }
  .brand-name .l2 { display: block; font-size: 56px; }
  .brand-name .l3 { display: block; font-size: 30px; margin-top: 6px; }

  .badge { position: absolute; left: 692px; top: 234px; width: 204px; height: 204px; }

  .intro { position: absolute; left: 58px; top: 356px; font-size: 37px; font-weight: 700; line-height: 1.3; }

  .services { position: absolute; left: 58px; top: 508px; list-style: none; }
  .services li { display: flex; align-items: center; gap: 10px; height: 45.3px; font-size: 27px; }
  .services li::before {
    content: ""; width: 18px; height: 18px; border-radius: 50%;
    background: var(--white); border: 4px solid var(--blue-light); flex: none;
  }

  .licence { position: absolute; left: 713px; top: 460px; font-size: 28px; }

  .hero-photo {
    position: absolute; left: 370px; top: 420px; width: 530px; height: 515px;
    background: radial-gradient(ellipse at 50% 45%, rgba(28,42,94,0.85), rgba(31,134,214,0) 70%);
  }

  .job-photo {
    position: absolute; width: 220px; height: 220px; border-radius: 50%;
    border: 5px solid var(--blue-light);
  }
  .job-photo.trench { left: 17px; top: 977px; background: linear-gradient(160deg, #8a6a4a, #b08a62 55%, #6e5238); }
  .job-photo.wall { left: 247px; top: 920px; background: linear-gradient(110deg, #9a4c35, #c9b7a0 45%, #8e4632); }

  .contact { position: absolute; left: 540px; top: 1010px; list-style: none; font-size: 28px; }
  .contact li { display: flex; align-items: flex-start; gap: 14px; margin-bottom: 14px; line-height: 1.25; }
  .contact svg { width: 28px; height: 28px; flex: none; margin-top: 4px; fill: var(--blue-light); }

  .website { position: absolute; left: 0; right: 0; top: 1225px; text-align: center; font-size: 29px; letter-spacing: 7px; }
</style>
</head>
<body>
<main class="flyer">
  <svg class="flyer-waves" viewBox="0 0 925 1310" preserveAspectRatio="none" aria-hidden="true">
    <path d="M0,270 C220,300 520,300 925,185 L925,1005 C700,960 450,990 250,1090 C150,1140 60,1170 0,1185 Z" fill="var(--blue-light)"/>
    <path d="M0,295 C220,335 520,330 925,215 L925,985 C700,940 450,970 250,1070 C150,1120 60,1150 0,1165 Z" fill="var(--blue)"/>
  </svg>

  <header class="brand">
    <span class="brand-dot"></span>
    <h1 class="brand-name">
      <span class="l1">7Brink</span>
      <span class="l2">Plumbing</span>
      <span class="l3">&amp; Air-Conditioning</span>
    </h1>
  </header>

  <svg class="badge" viewBox="0 0 204 204" aria-label="Emergency services 24/7, ready to respond">
    <defs>
      <path id="badge-top" d="M30,102 A72,72 0 0 1 174,102"/>
      <path id="badge-bottom" d="M24,108 A78,78 0 0 0 180,108"/>
    </defs>
    <circle cx="102" cy="102" r="100" fill="var(--white)"/>
    <circle cx="102" cy="102" r="52" fill="none" stroke="var(--blue)" stroke-width="6"/>
    <text font-family="Roboto Condensed, sans-serif" font-weight="700" font-size="24" fill="var(--navy)">
      <textPath href="#badge-top" startOffset="50%" text-anchor="middle">EMERGENCY SERVICES</textPath>
    </text>
    <text font-family="Roboto Condensed, sans-serif" font-weight="700" font-size="24" fill="var(--blue)">
      <textPath href="#badge-bottom" startOffset="50%" text-anchor="middle" dominant-baseline="hanging">READY TO RESPOND</textPath>
    </text>
    <text x="102" y="118" text-anchor="middle" font-family="Roboto Condensed, sans-serif" font-weight="700" font-size="46" fill="var(--navy)">24/7</text>
  </svg>

  <h2 class="intro">7BRINK Plumbing is a plumbing<br>business specializing in:</h2>

  <ul class="services">
    <li>Plumbing &amp; Gasfitting</li>
    <li>Air-Conditioning</li>
    <li>Blocked Drains</li>
    <li>Hot Water Systems</li>
    <li>Solar Hot Water Systems</li>
    <li>Central Heating</li>
    <li>Roofing</li>
    <li>Sanitary &amp; Drainage</li>
    <li>Renovations &amp; New Builds</li>
  </ul>

  <p class="licence">Lic #: 208417</p>

  <div class="hero-photo" role="img" aria-label="Smiling plumber in navy uniform holding a red pipe wrench and a tool bag, giving a thumbs up"></div>

  <div class="job-photo trench" role="img" aria-label="Drainage work in an excavated trench with pipes"></div>
  <div class="job-photo wall" role="img" aria-label="Hot water system and air-conditioning unit installed on a brick wall"></div>

  <ul class="contact">
    <li>
      <svg viewBox="0 0 24 24" aria-hidden="true"><path d="M6.6 10.8c1.4 2.8 3.8 5.1 6.6 6.6l2.2-2.2c.3-.3.7-.4 1-.2 1.1.4 2.3.6 3.6.6.6 0 1 .4 1 1V20c0 .6-.4 1-1 1C10.6 21 3 13.4 3 4c0-.6.4-1 1-1h3.5c.6 0 1 .4 1 1 0 1.3.2 2.5.6 3.6.1.3 0 .7-.2 1z"/></svg>
      <span>+61 400 582 117</span>
    </li>
    <li>
      <svg viewBox="0 0 24 24" aria-hidden="true"><path d="M2 5h20v2l-10 6L2 7zM2 9l10 6 10-6v10H2z"/></svg>
      <span>sam@7brinkplumbing.com</span>
    </li>
    <li>
      <svg viewBox="0 0 24 24" aria-hidden="true"><path d="M12 2a7 7 0 0 0-7 7c0 5 7 13 7 13s7-8 7-13a7 7 0 0 0-7-7zm0 9.5A2.5 2.5 0 1 1 12 6.5a2.5 2.5 0 0 1 0 5z"/></svg>
      <span>P.O Box 362 Kellerton, VIC<br>Australia 3900</span>
    </li>
  </ul>

  <p class="website">www.7brinkplumbing.com</p>
</main>
</body>
</html>
```